Halbrook & Company

We are a boutique commercial real estate firm. For our Business card design - sleek, modern, yet high-end/classy. Please see our website: halbrookandcompany.example for details.

We currently need 2 business card names and the ability to add/change the business card information -
Name, Title, Address, Office #, Mobile #, Fax, Email and company website.

Industry/Entity Type

Real Estate

Contact Information for Business Card

Business card design - sleek, modern, yet high-end/classy. Please see our website: halbrookandcompany.example for details.

Also, we'd like to have our slogan "Care Shapes Every Result." somewhere in there. We'd like to make some part of it raised or a different texture if possible.
Color #'s:
blue 19 36 128
light gray 222 222 221
dark gray 107 120 128

Also, we'd like to have our slogan "Care Shapes Every Result." somewhere in there. We'd like to make some part of it raised or a different texture if possible - grey on one side and blue on the other - rounded edges preferred. Maybe either metal/silver/grey raised logo on the back. Thank you!!

Requirements
Must have
• Sleek, modern, clean and classy design

```html
<!DOCTYPE html>
<html lang="en">
<head>
<meta charset="utf-8">
<title>Halbrook &amp; Company — Business Cards</title>
<link href="https://fonts.googleapis.com/css2?family=Oswald:wght@500;600&family=Open+Sans:wght@400;600&family=Playfair+Display:ital@0;1&display=swap" rel="stylesheet">
<style>
  :root {
    --brand-blue: #1e3ea8;
    --brand-blue-deep: #132480;
    --light-gray: #dedede;
    --card-gray: #b9bec8;
    --dark-gray: #6b7880;
    --ink: #ffffff;
    --stage: #2a2c30;
  }
  * { margin: 0; padding: 0; box-sizing: border-box; }
  html, body { width: 1200px; height: 900px; overflow: hidden; }
  body {
    background: var(--stage);
    position: relative;
    font-family: "Open Sans", sans-serif;
  }
  .card {
    position: absolute;
    top: 296px;
    width: 540px;
    height: 309px;
    border-radius: 22px;
    overflow: hidden;
  }

  /* Contact side */
  .card--front {
    left: 40px;
    background:
      radial-gradient(ellipse 260px 200px at 62% 58%, rgba(255,255,255,0.28), rgba(255,255,255,0) 100%),
      linear-gradient(160deg, #c4c8d1 0%, var(--card-gray) 60%, #aeb3be 100%);
  }
  .front__name {
    position: absolute; left: 32px; top: 26px;
    font-family: "Oswald", sans-serif; font-weight: 600;
    font-size: 24px; line-height: 32px; letter-spacing: 0.5px; color: var(--ink);
  }
  .front__title {
    position: absolute; left: 32px; top: 60px;
    font-family: "Playfair Display", serif; font-style: italic;
    font-size: 11px; color: var(--brand-blue);
  }
  .front__phones {
    position: absolute; left: 32px; top: 92px;
    list-style: none;
  }
  .front__phones li {
    display: flex; align-items: center; gap: 8px;
    font-size: 11px; color: var(--ink); height: 19px;
  }
  .front__phones svg { width: 11px; height: 11px; fill: var(--brand-blue); }
  .front__brand {
    position: absolute; right: 32px; top: 110px;
    display: flex; align-items: center; gap: 10px;
  }
  .front__brand-mark { width: 14px; height: 14px; background: var(--brand-blue); }
  .front__brand-name {
    font-family: "Oswald", sans-serif; font-weight: 600;
    font-size: 26px; line-height: 34px; color: var(--ink); letter-spacing: 0.5px;
  }
  .front__divider {
    position: absolute; left: 70px; right: 32px; top: 168px;
    height: 1px; background: var(--ink);
  }
  .front__address {
    position: absolute; right: 32px; top: 182px;
    list-style: none; text-align: right;
  }
  .front__address li {
    display: flex; align-items: flex-start; justify-content: flex-end; gap: 8px;
    font-size: 12px; line-height: 17px; color: var(--ink); margin-bottom: 4px;
  }
  .front__address svg { width: 11px; height: 11px; fill: var(--brand-blue); margin-top: 3px; }
  .front__band {
    position: absolute; left: 0; right: 0; bottom: 0; height: 44px;
    background: var(--brand-blue);
    display: flex; align-items: center; justify-content: center;
    font-size: 13px; color: var(--ink); letter-spacing: 0.3px;
  }

  /* Brand side */
  .card--back {
    left: 620px;
    background:
      radial-gradient(ellipse 240px 180px at 38% 45%, rgba(255,255,255,0.12), rgba(255,255,255,0) 100%),
      linear-gradient(150deg, #2b4cc0 0%, var(--brand-blue) 45%, var(--brand-blue-deep) 100%);
    display: flex; flex-direction: column; align-items: center; justify-content: center;
  }
  .back__brand {
    font-family: "Oswald", sans-serif; font-weight: 600;
    font-size: 40px; line-height: 52px; color: var(--ink); letter-spacing: 1px;
  }
  .back__rule { width: 240px; height: 1px; background: var(--ink); margin: 12px 0 10px; }
  .back__slogan {
    font-family: "Playfair Display", serif;
    font-size: 16px; color: var(--light-gray); letter-spacing: 0.3px;
  }
</style>
</head>
<body>
  <section class="card card--front" aria-label="Business card, contact side">
    <h1 class="front__name">YOUR NAME</h1>
    <p class="front__title">Job Title</p>
    <ul class="front__phones">
      <li><svg viewBox="0 0 12 12"><path d="M2 1h3l1 3-1.5 1a7 7 0 0 0 2.5 2.5L8 6l3 1v3a1 1 0 0 1-1 1A9 9 0 0 1 1 2a1 1 0 0 1 1-1z"/></svg>000 000 0000</li>
      <li><svg viewBox="0 0 12 12"><path d="M3.5 0h5a1 1 0 0 1 1 1v10a1 1 0 0 1-1 1h-5a1 1 0 0 1-1-1V1a1 1 0 0 1 1-1zm.5 1.5v8h4v-8z"/></svg>000 000 0000</li>
      <li><svg viewBox="0 0 12 12"><path d="M3 0h5l1 1v3h2v7H1V4h2zm1 1v3h4V1zM3 6v1h2V6zm4 0v1h2V6z"/></svg>000 000 0000</li>
    </ul>
    <div class="front__brand">
      <span class="front__brand-mark"></span>
      <span class="front__brand-name">Halbrook &amp; Company</span>
    </div>
    <div class="front__divider"></div>
    <ul class="front__address">
      <li><span>0000, Anywehre, Somewhere<br>City, ST 0000</span><svg viewBox="0 0 12 12"><path d="M6 0a4 4 0 0 1 4 4c0 3-4 8-4 8S2 7 2 4a4 4 0 0 1 4-4zm0 2.5a1.5 1.5 0 1 0 0 3 1.5 1.5 0 0 0 0-3z"/></svg></li>
      <li><span>youremail@xyz.com</span><svg viewBox="0 0 12 12"><path d="M0 2h12v8H0zm1 1v.5l5 3.5 5-3.5V3z"/></svg></li>
    </ul>
    <div class="front__band">www.halbrookandcompany.example</div>
  </section>

  <section class="card card--back" aria-label="Business card, brand side">
    <p class="back__brand">Halbrook &amp; Company</p>
    <div class="back__rule"></div>
    <p class="back__slogan">Care Shapes Every Result.</p>
  </section>
</body>
</html>
```